Business Card Design - Photographer

I am a landscape photographer and I require a business card design. 

I require two designs:
1)  a double sided business card
 and
b)  a single sided business card 

The single sided design can either be the same as the double sided (with just one side having all the information)....or it can be an entire new design. Its up to you.

My corporate colours are (CMYK):

Blue   69, 32, 0, 0
Grey  72,  64,  47,  31
Green  32,  2,  91,  0
Yellow   0, 19, 92, 0
Orange  0, 39, 75, 0

Colour space in final file should be in CMYK.

The details that need to be included on the card:

- Use the provided Logo
- Name: Lukas Wendrovski
- Email:   sales@vistaplume.com.au
- Website:    vistaplume.com.au
- Twitter:    chirpnet.com/vistaplume
- Facebook:   pinloop.com/vistaplume
- Mobile  0415 309 662

Please use the attached template to design the logo to the specified size, including the marked bleed lines. I have also attached my logo in PNG (transparent background) and ai format for you to use.

The final file should be:
- Photoshop version with layers so I can edit the name/text etc. All non vector files should be high resolution at 1039 x 697 pixels at 300 dpi.

I also require a file as:
- Vector based PDF

Anyway questions please contact me.

Thank you

Industry/Entity Type

Landscape

Logo styles of interest
Pictorial/Combination Logo
Abstract Logo
Wordmark Logo
Lettermark Logo
Requirements
Must have
• The details that need to be included on the card:

- Use the provided Logo
- Name: Lukas Wendrovski
- Email: sales@vistaplume.com.au
- Website: vistaplume.com.au
- Twitter: chirpnet.com/vistaplume
- Facebook: pinloop.com/vistaplume
- Mobile 0415 309 662

```html
<!DOCTYPE html>
<html lang="en">
<head>
<meta charset="utf-8">
<title>Vistaplume – Business Card</title>
<link rel="stylesheet" href="https://fonts.googleapis.com/css2?family=Cinzel:wght@500;600&family=Jura:wght@600&family=Saira+Semi+Condensed:wght@600&display=swap">
<style>
  :root {
    --slate: #44445a;
    --ink: #2c2c38;
    --orange: #f0a040;
    --gold: #f2a33a;
    --frame: #d4d4d4;
    --paper: #ffffff;
    --faint: #e4e4ea;
  }
  html, body { margin: 0; padding: 0; }
  body {
    width: 914px; height: 1200px; overflow: hidden;
    background: var(--paper); position: relative;
    font-family: "Saira Semi Condensed", sans-serif;
  }
  .sheet {
    position: absolute; left: 27px; width: 848px;
    background: var(--frame);
  }
  .sheet--front { top: 24px; height: 561px; }
  .sheet--back { top: 600px; height: 570px; }
  .bleed {
    position: absolute; inset: 22px 22px;
    border: 1.5px dotted #777; background: var(--paper);
  }
  .card { position: absolute; inset: 14px; border: 1.5px solid #555; overflow: hidden; }

  /* front */
  .front-band {
    position: absolute; left: 2px; right: 2px; top: 46px; height: 252px;
    background: var(--slate);
  }
  .front-disc {
    position: absolute; left: 236px; top: 0; width: 312px; height: 312px;
    border-radius: 50%; background: var(--paper);
  }
  .front-name {
    position: absolute; left: 0; right: 0; top: 338px; text-align: center;
    font-family: "Cinzel", serif; font-weight: 600; font-size: 54px;
    letter-spacing: 2px; color: var(--slate); line-height: 1;
  }
  .front-rule {
    position: absolute; left: 40px; right: 40px; top: 400px;
    height: 2px; background: var(--slate);
  }
  .front-tagline {
    position: absolute; left: 0; right: 0; top: 420px; text-align: center;
    font-family: "Cinzel", serif; font-weight: 500; font-size: 23px;
    letter-spacing: 5px; color: var(--slate);
  }

  /* back */
  .back-band {
    position: absolute; left: 2px; right: 10px; top: 6px; height: 112px;
    background: var(--slate);
  }
  .back-disc {
    position: absolute; left: 6px; top: 0; width: 124px; height: 124px;
    border-radius: 50%; background: var(--paper);
  }
  .back-name {
    position: absolute; left: 0; right: 0; top: 24px; text-align: center;
    padding-left: 150px;
    font-family: "Cinzel", serif; font-weight: 600; font-size: 38px;
    letter-spacing: 2px; color: var(--gold); line-height: 1;
  }
  .back-rule {
    position: absolute; left: 200px; right: 50px; top: 74px;
    height: 1.5px; background: var(--gold);
  }
  .back-tagline {
    position: absolute; left: 0; right: 0; top: 80px; text-align: center;
    padding-left: 150px;
    font-family: "Cinzel", serif; font-weight: 500; font-size: 17px;
    letter-spacing: 3px; color: var(--gold);
  }
  .backdrop-disc {
    position: absolute; left: 405px; top: 200px; width: 340px; height: 340px;
    border-radius: 50%; background: var(--faint);
  }
  .person {
    position: absolute; left: 0; right: 0; top: 222px; text-align: center;
    padding-right: 30px;
    font-family: "Jura", sans-serif; font-weight: 600; font-size: 46px;
    letter-spacing: 2px; color: var(--orange);
  }
  .contacts {
    position: absolute; left: 4px; top: 300px; margin: 0; padding: 0;
    list-style: none;
  }
  .contacts li {
    display: flex; align-items: center; gap: 5px;
    height: 38px; font-size: 29px; color: var(--ink); line-height: 1;
  }
  .contacts svg { width: 24px; height: 24px; flex: none; fill: var(--ink); }
</style>
</head>
<body>

<section class="sheet sheet--front" aria-label="Card front">
  <div class="bleed">
    <div class="card">
      <div class="front-band"></div>
      <div class="front-disc"></div>
      <div class="front-name">VISTAPLUME</div>
      <div class="front-rule"></div>
      <div class="front-tagline">FINE ART PHOTOGRAPHY</div>
    </div>
  </div>
</section>

<section class="sheet sheet--back" aria-label="Card back">
  <div class="bleed">
    <div class="card">
      <div class="backdrop-disc"></div>
      <div class="back-band"></div>
      <div class="back-disc"></div>
      <div class="back-name">VISTAPLUME</div>
      <div class="back-rule"></div>
      <div class="back-tagline">FINE ART PHOTOGRAPHY</div>
      <div class="person">Lukas Wendrovski</div>
      <ul class="contacts">
        <li><svg viewBox="0 0 24 24"><circle cx="12" cy="12" r="11"/></svg>vistaplume.com.au</li>
        <li><svg viewBox="0 0 24 24"><rect x="6" y="2" width="12" height="20" rx="2"/><rect x="8" y="5" width="8" height="8" fill="#fff"/></svg>0415 309 662</li>
        <li><svg viewBox="0 0 24 24"><rect x="1" y="5" width="22" height="14"/><path d="M2 6 L12 13 L22 6" stroke="#fff" stroke-width="2" fill="none"/></svg>sales@vistaplume.com.au</li>
        <li><svg viewBox="0 0 24 24"><rect x="2" y="2" width="20" height="20" rx="2"/></svg>pinloop.com/vistaplume</li>
        <li><svg viewBox="0 0 24 24"><rect x="2" y="2" width="20" height="20" rx="2"/></svg>chirpnet.com/vistaplume</li>
      </ul>
    </div>
  </div>
</section>

</body>
</html>
```